International Dating Community Needs a Web Design

We need a single page web design built on plomet.com. Designers need to design a one page web design on PLOMET, take a screenshot and paste it here. Once the winner is chosen, the designer needs to give me access to the design and transfer over the implementation.
REQUIREMENTS:
- Designer MUST design on plomet.com (http://www.plomet.com/support/main/html5/getting-started/signing-free)
- Once designed, designer needs to take a screenshot of the plomet design and submit the design on artvessel.
- Please add the site url as the design comment when you submit the design
- Any designers that use existing PLOMET templates will NOT be eligible to win and will be eliminated.
Note: If you use any stock images, simply let me know the numbers and I will purchase them.
PAGE INFORMATION:
Color Scheme:
- Light Blue / Cyan
- White
- Black / Dark Gray
Header:
- Logo (attached) on the left
- Login / Register on the right
Navigation bar:
- Home
- Events
- Entertainment / Music
- Gallery
- Membership
- About Us
Homepage Content:
The worlds #1 destination for international dating!
We may be new to you, but our team have been around for longer than you think. We're here to promote upcoming cultural events in your community, promote local businesses serving your community & soon we will also be offering an online dating service to meet others within the area.
If you're interested in learning more about events & concerts relating to the community then make sure you like us on Chatterbox.
If you have any comments or feedback, we'd love to hear from you! Click here to contact us.
Photos:
Im open for you to use any photos you like - some sites I like:
http://www.openpicturebank.net/images/People_g40.html
http://www.qvr.hu/category/135

```html
<!DOCTYPE html>
<html lang="en">
<head>
<meta charset="utf-8">
<title>linqora – International Dating Community</title>
<link href="https://fonts.googleapis.com/css2?family=Arimo:wght@400;700&display=swap" rel="stylesheet">
<style>
  :root {
    --teal: #33b0a3;
    --teal-light: #9ad8d2;
    --teal-brand: #4ecfbe;
    --header-top: #383838;
    --header-bottom: #5fc4b6;
    --ink: #000000;
    --paper: #ffffff;
  }
  * { box-sizing: border-box; margin: 0; padding: 0; }
  html, body {
    width: 1200px;
    height: 1055px;
    overflow: hidden;
    background: var(--paper);
    font-family: "Arimo", Arial, sans-serif;
    color: var(--ink);
  }
  .page { position: relative; width: 1200px; height: 1055px; }

  .site-header {
    position: absolute; left: 38px; top: 32px;
    width: 1124px; height: 234px;
    background: linear-gradient(to bottom, var(--header-top) 0%, #4b6f6a 45%, var(--header-bottom) 100%);
  }
  .brand {
    position: absolute; left: 38px; top: 80px;
    font-family: "Arimo", Arial, sans-serif; font-weight: 400;
    font-size: 34px; line-height: 38px; color: var(--teal-brand);
  }
  .brand-tagline {
    position: absolute; left: 39px; top: 121px;
    font-family: "Arimo", Arial, sans-serif; font-weight: 400;
    font-size: 16px; line-height: 20px; color: var(--teal-brand);
  }
  .account-actions { position: absolute; right: 38px; top: 14px; display: flex; gap: 6px; }
  .account-button {
    width: 121px; height: 50px; background: var(--teal); color: var(--paper);
    border-radius: 2px; font-size: 20px; line-height: 50px; text-align: center;
  }
  .main-nav {
    position: absolute; right: 38px; top: 195px;
    font-size: 21px; color: var(--paper); white-space: nowrap;
  }

  .photo-slider {
    position: absolute; left: 38px; top: 272px;
    width: 352px; height: 424px; background: var(--teal-light);
  }
  .slider-arrow { position: absolute; top: 187px; width: 42px; height: 46px; }
  .slider-arrow.prev { left: 3px; }
  .slider-arrow.next { right: 3px; }
  .photo-caption {
    position: absolute; left: 0; right: 0; bottom: 8px;
    text-align: center; font-size: 35px;
  }

  .welcome { position: absolute; left: 390px; width: 730px; top: 388px; text-align: center; }
  .welcome-title { font-size: 68px; font-weight: 700; line-height: 76px; }
  .welcome-subtitle { font-size: 35px; font-weight: 400; line-height: 38px; }

  .search-field {
    position: absolute; left: 407px; top: 638px;
    width: 557px; height: 57px; border: 2px solid var(--ink);
    border-radius: 3px; background: var(--paper);
  }
  .search-button {
    position: absolute; left: 984px; top: 638px;
    width: 139px; height: 57px; background: var(--teal); color: var(--paper);
    border-radius: 2px; font-size: 35px; line-height: 57px; text-align: center;
  }

  .homepage-content {
    position: absolute; left: 39px; top: 735px;
    width: 1124px; height: 340px; background: var(--teal-light);
    border-radius: 3px 3px 0 0; overflow: hidden;
  }
  .content-title {
    position: absolute; left: 36px; top: 16px;
    font-size: 42px; font-weight: 700;
  }
  .content-body {
    position: absolute; left: 174px; top: 108px; width: 880px;
    font-size: 42px; font-weight: 700; line-height: 48px;
  }
  .content-body p + p { margin-top: 56px; }
</style>
</head>
<body>
<div class="page">
  <header class="site-header">
    <div class="brand">linqora</div>
    <div class="brand-tagline">international dating community</div>
    <div class="account-actions">
      <span class="account-button">Login</span>
      <span class="account-button">Register</span>
    </div>
    <nav class="main-nav">Home | Events | Entertainment | Gallery | Membership | About Us</nav>
  </header>

  <section class="photo-slider" role="img" aria-label="Photo slider area for community photos">
    <svg class="slider-arrow prev" viewBox="0 0 42 46" aria-hidden="true"><polygon points="30,2 40,10 22,23 40,36 30,44 4,23" fill="#000"/></svg>
    <svg class="slider-arrow next" viewBox="0 0 42 46" aria-hidden="true"><polygon points="12,2 2,10 20,23 2,36 12,44 38,23" fill="#000"/></svg>
    <div class="photo-caption">Example Photo</div>
  </section>

  <section class="welcome">
    <h1 class="welcome-title">Welcome to linqora</h1>
    <p class="welcome-subtitle">International Dating Community</p>
  </section>

  <div class="search-field"></div>
  <div class="search-button">Search</div>

  <main class="homepage-content">
    <h2 class="content-title">Homepage:</h2>
    <div class="content-body">
      <p>The worlds #1 destination for international dating!</p>
      <p>We may be new to you, but our team have been around for longer than you think.</p>
    </div>
  </main>
</div>
</body>
</html>
```